ZEPRILO.COM is a premium domain sales company. Our competitors are companies like vastplots.example, getparcels.example, peerwords.example. Our current site is at www.zeprilos.example.

We want to have the ability to search for domains, to highlight special offers and have some testimonials on the index page.

The logo for the site is attached.

Please be sure that the order form fits on the screen without scrolling the page. I want the entire form, including the submit button to fit without any page scrolling.

Delivered product - INDEX PAGE, ORDER FORM AND CONTENT PAGE PSDs.

Target Market(s)

Small to Medium business professionals

Industry/Entity Type

It Company

Requirements
Must have
• 1. List of domains for sale
2. Simple search box with button to run the search
3. link for advanced search
4. testimonial area. Note - this can be a small box where a different testimonial is displayed on each page load.
Nice to have
• Would like the site to have some white space. Don't want a heavily packed website. Give it an "airy" feel.

```html
<!DOCTYPE html>
<html lang="en">
<head>
<meta charset="utf-8">
<title>ZEPRILO.COM – Premium Domains</title>
<link href="https://fonts.googleapis.com/css2?family=Montserrat:wght@400;500;600;700&family=Arimo:wght@400;700&display=swap" rel="stylesheet">
<style>
:root{
  --green-dark:#0f5f27;
  --green-field:#0b4a1e;
  --blue-title:#1a56a6;
  --nav-active:#bfe1f6;
  --ink:#333;
  --page:#efefef;
  --panel-dark:#2f3234;
  --muted:#8e9a9c;
  --offer-red:#d10f0f;
  --offer-olive:#c4b300;
  --offer-black:#0a0a0a;
  --footer:#262626;
  --footer-box:#3b3b3b;
  --gold:#d9bc00;
  --white:#fff;
}
*{box-sizing:border-box;margin:0;padding:0}
html,body{width:1200px;height:1063px;overflow:hidden}
body{position:relative;background:var(--page);font-family:"Montserrat",sans-serif;color:var(--ink)}
.abs{position:absolute}

/* top bar */
.topbar{left:0;top:0;width:1200px;height:22px;background:var(--green-dark);color:var(--white);font-size:10px}
.topbar .item{position:absolute;top:4px;display:flex;align-items:center;gap:8px}
.topbar .search{position:absolute;left:889px;top:2px;width:280px;height:18px;background:var(--green-field);border-radius:2px;padding:3px 12px;font-size:10px}
.topbar .search svg{position:absolute;right:8px;top:3px}

/* header */
.header{left:0;top:22px;width:1200px;height:44px;background:var(--white)}
.logo{position:absolute;left:39px;top:6px;display:flex;align-items:center;gap:8px;font-weight:700;font-size:27px;color:#1d6b2c}
.logo .dot{width:14px;height:14px;border-radius:50%;background:#1d6b2c}
.nav-active{left:401px;top:16px;width:80px;height:17px;background:var(--nav-active)}
.nav-label{position:absolute;top:14px;font-size:15px;font-weight:400;color:#222;letter-spacing:.3px}

/* hero */
.hero{left:0;top:66px;width:1200px;height:273px;background:linear-gradient(90deg,#3a4a5c 0%,#1c2633 35%,#2e3c4a 55%,#202a35 75%,#5b6d80 100%)}
.search-panel{left:38px;top:104px;width:560px;height:191px}
.search-panel svg.shape{position:absolute;left:0;top:0}
.sp-title{left:24px;top:8px;font-size:22px;font-weight:700;color:var(--blue-title);letter-spacing:.5px}
.sp-sub{left:48px;top:35px;font-size:11px;font-style:italic;color:#2c64ad}
.sp-input{left:23px;top:53px;width:460px;height:28px;background:var(--white);border:1px solid #c8c8c8;border-radius:3px 0 0 3px}
.sp-go{left:483px;top:53px;width:61px;height:28px;background:linear-gradient(#fafafa,#dcdcdc);border:1px solid #bbb;border-radius:0 3px 3px 0;font-size:11px;font-weight:600;text-align:center;line-height:26px;color:#444}
.sp-hint{left:36px;top:86px;font-size:8.5px;font-style:italic;color:#275a9a}
.sp-adv{left:36px;top:98px;font-size:12.5px;font-weight:700;color:var(--white);letter-spacing:.5px;border-bottom:1px solid rgba(255,255,255,.6)}
.pay-badge{left:172px;top:140px;width:138px;height:22px;border-radius:4px;background:#1f3f8a}
.cards{left:94px;top:169px;display:flex;gap:5px}
.cards span{display:block;width:40px;height:19px;border-radius:2px}

/* domains list */
.section-title{font-size:23px;font-weight:500;color:var(--blue-title);letter-spacing:.3px}
.domains{left:38px;top:371px;width:1134px;height:127px}
.domains svg.shape{position:absolute;left:0;top:0}
.cat{position:absolute;width:340px}
.cat .icon{position:absolute;left:0;top:0;width:37px;height:26px;border-radius:50%;background:var(--white);display:flex;align-items:center;justify-content:center}
.cat h3{position:absolute;left:50px;top:3px;font-size:14.5px;font-weight:500;color:var(--white);letter-spacing:.5px}
.cat p{position:absolute;left:56px;top:24px;width:300px;font-size:10.6px;line-height:12.5px;color:var(--muted);letter-spacing:.4px}

/* testimonials */
.quote{position:absolute;width:369px;height:98px;background:var(--white);padding:7px 14px 0 19px;font-family:"Montserrat",sans-serif;font-weight:500;font-size:12.6px;line-height:12.3px;color:#3e3e3e}
.quote::after{content:"";position:absolute;left:20px;bottom:-8px;border-left:8px solid transparent;border-right:8px solid transparent;border-top:8px solid var(--white)}
.author{position:absolute;font-size:13px;font-weight:600;color:#222;display:flex;align-items:center;gap:8px}
.author small{font-weight:400;font-size:10px;color:#a6a6a6}

/* offers */
.offer{position:absolute;left:829px;width:345px;text-align:center;font-family:"Arimo",sans-serif;text-transform:uppercase;line-height:1;overflow:hidden}
.offer.red{top:539px;height:46px;background:var(--offer-red);color:var(--white);padding-top:3px}
.offer.olive1{top:596px;height:51px;background:var(--offer-olive);color:#111;padding-top:9px}
.offer.black{top:657px;height:49px;background:var(--offer-black);color:var(--white);padding-top:3px}
.offer.olive2{top:717px;height:48px;background:var(--offer-olive);color:#111;padding-top:3px}

/* footer */
.footer{left:0;top:801px;width:1200px;height:262px;background:var(--footer);color:#ddd}
.f-head{position:absolute;top:20px;font-size:14.5px;font-weight:600;color:var(--gold);letter-spacing:.4px}
.contact-row{position:absolute;left:37px;width:265px;font-size:11.5px;color:#e6e6e6;padding-bottom:5px;border-bottom:1px solid #3a3a3a}
.contact-row b{font-weight:600}
.social{position:absolute;left:83px;top:173px;display:flex;gap:8px}
.social span{display:block;width:26px;height:15px;border-radius:50%}
.update{position:absolute;left:338px;width:265px;height:60px;background:var(--footer-box);padding:6px 10px;font-size:10.5px;line-height:12px;color:#e6e6e6}
.update::after{content:"";position:absolute;left:120px;bottom:-6px;border-left:6px solid transparent;border-right:6px solid transparent;border-top:6px solid var(--footer-box)}
.cat-list{position:absolute;left:639px;top:59px;width:266px}
.cat-list li{list-style:none;height:18px;margin-bottom:1.3px;background:var(--footer-box);padding-left:10px;font-size:10.5px;line-height:18px;color:#e6e6e6}
.nl-text{position:absolute;left:941px;top:66px;width:250px;font-size:11px;line-height:13px;color:#e6e6e6}
.nl-row{position:absolute;left:941px;height:28px;display:flex;gap:18px}
.nl-row .ico{width:46px;height:100%;background:var(--footer-box);display:flex;align-items:center;justify-content:center}
.nl-row .field{width:195px;height:100%;background:var(--footer-box);padding-left:18px;font-size:11px;line-height:28px;color:#bbb}
.submit{position:absolute;left:1115px;top:183px;width:85px;height:27px;background:var(--footer-box);font-size:11.5px;line-height:27px;text-align:center;color:#ddd}
.copyright{position:absolute;left:45px;top:231px;font-size:11.5px;color:#ddd}
.f-rule{position:absolute;left:37px;top:248px;width:1163px;height:1px;background:#3a3a3a}
</style>
</head>
<body>

<!-- top bar -->
<div class="abs topbar">
  <div class="item" style="left:38px">
    <svg width="10" height="12" viewBox="0 0 10 12"><path d="M5 0a4 4 0 0 0-4 4c0 3 4 8 4 8s4-5 4-8a4 4 0 0 0-4-4z" fill="#0a4a1c"/><circle cx="5" cy="4" r="1.5" fill="#fff"/></svg>
    <span>12 Orchard Row, Lakeview, USA</span>
  </div>
  <div class="item" style="left:232px">
    <svg width="10" height="12" viewBox="0 0 10 12"><path d="M2 0h2l1 3-1.5 1a6 6 0 0 0 3 4L8 7l2 1v2l-1 2C4 12 0 7 0 2z" fill="#0a4a1c"/></svg>
    <span>+000-555-0142</span>
  </div>
  <div class="item" style="left:375px">
    <svg width="30" height="12" viewBox="0 0 30 12"><rect x="1" y="1" width="28" height="10" fill="#0a4a1c"/><path d="M1 1l14 6 14-6" stroke="#156b2a" fill="none"/></svg>
    <span>info@zeprilo.example</span>
  </div>
  <div class="search">Search.
    <svg width="12" height="12" viewBox="0 0 12 12"><circle cx="5" cy="5" r="3.5" stroke="#2c7a3f" stroke-width="1.5" fill="none"/><path d="M8 8l3 3" stroke="#2c7a3f" stroke-width="1.5"/></svg>
  </div>
</div>

<!-- header -->
<header class="abs header">
  <div class="logo"><span class="dot"></span>ZEPRILO.COM</div>
  <div class="abs nav-active"></div>
  <nav>
    <span class="nav-label" style="left:416px">Home</span>
    <span class="nav-label" style="left:500px">Categories</span>
    <span class="nav-label" style="left:626px">Sell Your Domains</span>
    <span class="nav-label" style="left:817px">Domains for sale</span>
    <span class="nav-label" style="left:996px">Hosting</span>
    <span class="nav-label" style="left:1097px">Support</span>
  </nav>
</header>

<!-- hero -->
<div class="abs hero" role="img" aria-label="Photo of illuminated server racks in a data centre"></div>

<section class="abs search-panel">
  <svg class="shape" width="560" height="191" viewBox="0 0 560 191">
    <defs><linearGradient id="panelFill" x1="0" y1="0" x2="0" y2="1"><stop offset="0" stop-color="#b9dcf3"/><stop offset="1" stop-color="#d6ecf9"/></linearGradient></defs>
    <path d="M10 0H550A10 10 0 0 0 560 10V181A10 10 0 0 0 550 191H10A10 10 0 0 0 0 181V10A10 10 0 0 0 10 0Z" fill="url(#panelFill)"/>
  </svg>
  <h1 class="abs sp-title">Find Your Domain</h1>
  <p class="abs sp-sub">You can find the best name for your business...</p>
  <div class="abs sp-input"></div>
  <div class="abs sp-go">GO</div>
  <p class="abs sp-hint">Start your search by entering the first character of the domain name.</p>
  <a class="abs sp-adv">Advanced Search</a>
  <div class="abs pay-badge"></div>
  <div class="abs cards">
    <span style="background:#1d4fa0"></span>
    <span style="background:#c8201e"></span>
    <span style="background:#2d7dc4"></span>
    <span style="background:#e8e8e8"></span>
    <span style="background:#f2f2f2;border:1px solid #9ab"></span>
  </div>
</section>

<!-- domains for sale -->
<h2 class="abs section-title" style="left:38px;top:341px">List of domains for sale</h2>
<section class="abs domains">
  <svg class="shape" width="1134" height="127" viewBox="0 0 1134 127">
    <path d="M12 0H1122A12 12 0 0 0 1134 12V115A12 12 0 0 0 1122 127H12A12 12 0 0 0 0 115V12A12 12 0 0 0 12 0Z" fill="var(--panel-dark)"/>
  </svg>
  <div class="cat" style="left:7px;top:10px"><span class="icon"><svg width="20" height="12"><ellipse cx="10" cy="6" rx="9" ry="5" fill="none" stroke="#333" stroke-width="1.5"/><circle cx="10" cy="6" r="2.5" fill="#333"/></svg></span><h3>Special Categories</h3><p>Lorem dipiscing leo vel amet suscipit nulla<br>to leo mollis lorem alido macus purus.</p></div>
  <div class="cat" style="left:391px;top:10px"><span class="icon"><svg width="18" height="14"><rect x="1" y="1" width="16" height="10" fill="none" stroke="#333" stroke-width="1.5"/><path d="M6 13h6" stroke="#333" stroke-width="1.5"/></svg></span><h3>Business</h3><p>Lorem dipiscing leo vel amet suscipit nulla<br>to leo mollis lorem alido macus purus.</p></div>
  <div class="cat" style="left:773px;top:10px"><span class="icon"><svg width="20" height="14"><rect x="1" y="1" width="18" height="12" fill="none" stroke="#333" stroke-width="1.5"/><path d="M4 5h12M4 9h12" stroke="#333"/></svg></span><h3>Careers</h3><p>Lorem dipiscing leo vel amet suscipit nulla<br>to leo mollis lorem alido macus purus.</p></div>
  <div class="cat" style="left:7px;top:69px"><span class="icon"><svg width="18" height="16"><circle cx="7" cy="7" r="5" fill="none" stroke="#333" stroke-width="2" stroke-dasharray="2 1.5"/><circle cx="13" cy="11" r="3.5" fill="none" stroke="#333" stroke-width="1.5"/></svg></span><h3>Shopping</h3><p>Lorem dipiscing leo vel amet suscipit nulla<br>to leo mollis lorem alido macus purus.</p></div>
  <div class="cat" style="left:391px;top:69px"><span class="icon"><svg width="18" height="18" viewBox="0 0 18 18"><path d="M9 1l2.4 5 5.4.6-4 3.7 1.1 5.4L9 13l-4.9 2.7 1.1-5.4-4-3.7 5.4-.6z" fill="none" stroke="#333" stroke-width="1.5"/></svg></span><h3>Society</h3><p>Lorem dipiscing leo vel amet suscipit nulla<br>to leo mollis lorem alido macus purus.</p></div>
  <div class="cat" style="left:773px;top:69px"><span class="icon"><svg width="20" height="16"><ellipse cx="10" cy="8" rx="8" ry="6" fill="none" stroke="#333" stroke-width="1.5"/><circle cx="7" cy="8" r="1" fill="#333"/><circle cx="10" cy="8" r="1" fill="#333"/><circle cx="13" cy="8" r="1" fill="#333"/></svg></span><h3>Education</h3><p>Lorem dipiscing leo vel amet suscipit nulla<br>to leo mollis lorem alido macus purus.</p></div>
</section>

<!-- testimonials -->
<h2 class="abs section-title" style="left:38px;top:509px">Testimonial</h2>

<blockquote class="quote" style="left:44px;top:540px">Lorem ipsum dolor sit amet, consecer<br>adipiscing elit, sed diam noummy nibh<br>euismod tincidunt ut laoreet dolore<br>magna aliquam erat volutpat. Ut wisi<br>enim ad minim veniam, quis nostrud<br>exerci tation ullamcorper.</blockquote>
<div class="author" style="left:62px;top:644px"><svg width="12" height="10"><rect x="0" y="4" width="3" height="6" fill="#333"/><path d="M4 4l3-4h1v3h4v7H4z" fill="#333"/></svg>Mira Stone, <small>Little Crew Studio</small></div>

<blockquote class="quote" style="left:437px;top:540px">Lorem ipsum dolor sit amet, consecer<br>adipiscing elit, sed diam noummy nibh<br>euismod tincidunt ut laoreet dolore<br>magna aliquam erat volutpat. Ut wisi<br>enim ad minim veniam, quis nostrud<br>exerci tation ullamcorper.</blockquote>
<div class="author" style="left:456px;top:644px"><svg width="12" height="10"><rect x="0" y="4" width="3" height="6" fill="#333"/><path d="M4 4l3-4h1v3h4v7H4z" fill="#333"/></svg>Mira Stone, <small>Little Crew Studio</small></div>

<blockquote class="quote" style="left:44px;top:670px">Lorem ipsum dolor sit amet, consecer<br>adipiscing elit, sed diam noummy nibh<br>euismod tincidunt ut laoreet dolore<br>magna aliquam erat volutpat. Ut wisi<br>enim ad minim veniam, quis nostrud<br>exerci tation ullamcorper.</blockquote>
<div class="author" style="left:62px;top:774px"><svg width="12" height="10"><rect x="0" y="4" width="3" height="6" fill="#333"/><path d="M4 4l3-4h1v3h4v7H4z" fill="#333"/></svg>Mira Stone, <small>Little Crew Studio</small></div>

<blockquote class="quote" style="left:437px;top:670px">Lorem ipsum dolor sit amet, consecer<br>adipiscing elit, sed diam noummy nibh<br>euismod tincidunt ut laoreet dolore<br>magna aliquam erat volutpat. Ut wisi<br>enim ad minim veniam, quis nostrud<br>exerci tation ullamcorper.</blockquote>
<div class="author" style="left:456px;top:774px"><svg width="12" height="10"><rect x="0" y="4" width="3" height="6" fill="#333"/><path d="M4 4l3-4h1v3h4v7H4z" fill="#333"/></svg>Mira Stone, <small>Little Crew Studio</small></div>

<!-- offers -->
<div class="offer red"><div style="font-size:11px">Domains for just</div><div style="font-size:22px;font-weight:700">$1.99*</div><div style="font-size:11px">With a new, non-domain purchase</div></div>
<div class="offer olive1"><div style="font-size:16px;font-weight:700;letter-spacing:.5px">Already own a domain?</div><div style="font-size:14px;margin-top:3px">Add hosting, email and more.</div></div>
<div class="offer black"><div style="font-size:22px;font-weight:700;letter-spacing:.5px">Compare our</div><div style="font-size:22px;font-weight:700">domain prices!</div></div>
<div class="offer olive2"><div style="font-size:19px;font-weight:700">$3.99 .US</div><div style="font-size:11.5px">Save on specially</div><div style="font-size:11.5px">priced .US domains!</div></div>

<!-- footer -->
<footer class="abs footer">
  <h4 class="f-head" style="left:35px">Contact Us</h4>
  <h4 class="f-head" style="left:340px">Latest Updates</h4>
  <h4 class="f-head" style="left:637px">Categories</h4>
  <h4 class="f-head" style="left:941px">Newsletter Subscribe</h4>

  <div class="contact-row" style="top:75px"><b>Office:</b> 12 Orchard Row, Lakeview, USA</div>
  <div class="contact-row" style="top:96px"><b>e-Mail:</b> info@zeprilo.example</div>
  <div class="contact-row" style="top:120px"><b>Phone:</b> +000-555-0142</div>
  <div class="contact-row" style="top:144px;border:0"><b>Fax:</b> +000-555-0143</div>
  <div class="social"><span style="background:#2a6fc0"></span><span style="background:#3b6fd0"></span><span style="background:#29a3e0"></span><span style="background:#e0457a"></span><span style="background:#d4252e"></span></div>

  <div class="update" style="top:61px">Lorem ipsum dolor sit amet, consec-tetuer adipiscing elit, sed diam nonummy nibh euismod tincidunt ut laoreet.</div>
  <div class="update" style="top:139px">Lorem ipsum dolor sit amet, consec-tetuer adipiscing elit, sed diam nonummy nibh euismod tincidunt ut laoreet.</div>

  <ul class="cat-list">
    <li>Lorem ipsum</li><li>Lorem ipsum</li><li>Lorem ipsum</li><li>Lorem ipsum</li>
    <li>Lorem ipsum</li><li>Lorem ipsum</li><li>Lorem ipsum</li><li>Lorem ipsum</li>
  </ul>

  <p class="nl-text">Lorem ipsum dolor sit amet, consec-tetuer adipiscing elit.</p>
  <div class="nl-row" style="top:104px"><span class="ico"><svg width="16" height="12"><rect x="1" y="2" width="14" height="9" fill="none" stroke="#eee" stroke-width="1.5"/><path d="M4 0v3M12 0v3" stroke="#eee" stroke-width="1.5"/></svg></span><span class="field">First name</span></div>
  <div class="nl-row" style="top:144px;height:26px"><span class="ico"><svg width="16" height="11"><rect x="0" y="0" width="16" height="11" fill="#eee"/><path d="M0 0l8 6 8-6" stroke="#3b3b3b" fill="none"/></svg></span><span class="field" style="line-height:26px">Your e-mail</span></div>
  <div class="submit">Submit</div>

  <p class="copyright">© 2013 Zeprilo.com. All rights reserved.</p>
  <div class="f-rule"></div>
</footer>

</body>
</html>
```